Tide Hollow Sticker Design for LEAN 4

ur business name is ' Tide Hollow ' ( Logo attached ).
The Product is called ' Lean 4 ' It has six ingredients that need to be listed on the sticker - Chia, Turmeric, Ginger, Dandelion, Macha and Seaweed.
120 capsules in a packet.
I would like it to say the product is a ' Weight loss alternative ' ' all organic ingredients ' All natural '

The logo.

Project Deadline Extended Reason: I would love to see a few more designs please. I have also just guaranteed the project. Thank you. TIDE HOLLOW x Added Tuesday, October 31, 2017

Target Market(s)

Everyone.

Industry/Entity Type

Health And Wellness

Requirements
Must have
• ur business name is ' Tide Hollow ' ( Logo attached ).
• The Product is called ' Lean 4 ' It has six ingredients that need to be listed on the sticker - Chia, Turmeric, Ginger, Dandelion, Macha and Seaweed.
• 120 capsules in a packet.
• I would like it to say the product is a ' Weight loss alternative ' ' all organic ingredients ' All natural '
• The logo.
Nice to have
• A catchy image symbolising nature.

```html
<!DOCTYPE html>
<html lang="en">
<head>
<meta charset="utf-8">
<title>Tide Hollow – Lean 4 Sticker</title>
<link href="https://fonts.googleapis.com/css2?family=Archivo+Black&family=Cinzel:wght@600;700&family=Lobster+Two:ital,wght@1,700&family=Oswald:wght@400&display=swap" rel="stylesheet">
<style>
  :root {
    --page: #ffffff;
    --sticker: #acd9bc;
    --leaf: #0e8f44;
    --leaf-dark: #08642d;
    --leaf-brand: #1a8a45;
    --band: #7ccfdc;
    --ink: #111111;
    --white: #ffffff;
  }
  html, body {
    margin: 0;
    padding: 0;
    width: 1200px;
    height: 1184px;
    overflow: hidden;
    background: var(--page);
  }
  .sticker {
    position: absolute;
    left: 2px;
    top: 2px;
    width: 1196px;
    height: 1180px;
    border-radius: 140px;
    background: var(--sticker);
    overflow: hidden;
  }
  .brand {
    position: absolute;
    top: 92px;
    left: 0;
    width: 100%;
    text-align: center;
    font-family: "Oswald", sans-serif;
    font-weight: 400;
    font-size: 64px;
    color: var(--leaf-brand);
    letter-spacing: 1px;
    line-height: 1;
  }
  .claim {
    position: absolute;
    top: 222px;
    left: 0;
    width: 100%;
    text-align: center;
    font-family: "Cinzel", serif;
    font-weight: 700;
    font-size: 38px;
    color: var(--white);
    text-shadow: 3px 4px 5px rgba(0,0,0,0.35);
    letter-spacing: 0.5px;
  }
  .product-name {
    position: absolute;
    top: 350px;
    left: 0;
    width: 100%;
    text-align: center;
    font-family: "Lobster Two", cursive;
    font-style: italic;
    font-weight: 700;
    font-size: 270px;
    line-height: 1;
    color: var(--leaf);
    text-shadow: 3px 3px 0 var(--leaf-dark), 6px 6px 0 var(--leaf-dark), 9px 9px 0 var(--leaf-dark);
  }
  .ingredient {
    position: absolute;
    width: 100px;
    height: 100px;
    margin: -50px 0 0 -50px;
  }
  .ingredient-dot {
    position: absolute;
    inset: 0;
    border-radius: 50%;
    background: var(--leaf);
    box-shadow: 4px 5px 6px rgba(0,0,0,0.35);
  }
  .ingredient-name {
    position: absolute;
    left: 50%;
    top: 50%;
    transform: translate(-50%, -50%);
    white-space: nowrap;
    font-family: "Cinzel", serif;
    font-weight: 600;
    font-size: 30px;
    color: var(--ink);
  }
  .benefit-band {
    position: absolute;
    left: 0;
    top: 856px;
    width: 100%;
    height: 88px;
    background: var(--band);
    display: flex;
    align-items: center;
    justify-content: center;
  }
  .benefit {
    font-family: "Archivo Black", sans-serif;
    font-size: 62px;
    color: var(--leaf);
    letter-spacing: 0.5px;
    white-space: pre;
  }
  .count {
    position: absolute;
    top: 1076px;
    left: 0;
    width: 100%;
    text-align: center;
    font-family: "Cinzel", serif;
    font-weight: 700;
    font-size: 32px;
    color: var(--ink);
  }
</style>
</head>
<body>
  <div class="sticker">
    <div class="brand">Tide Hollow</div>
    <div class="claim">All Natural - All Organic Ingredients</div>
    <div class="product-name">Lean 4</div>

    <div class="ingredient" style="left:105px; top:625px;"><div class="ingredient-dot"></div><span class="ingredient-name">Seaweed</span></div>
    <div class="ingredient" style="left:307px; top:743px;"><div class="ingredient-dot"></div><span class="ingredient-name">Dandelion</span></div>
    <div class="ingredient" style="left:498px; top:689px;"><div class="ingredient-dot"></div><span class="ingredient-name">Chia</span></div>
    <div class="ingredient" style="left:695px; top:689px;"><div class="ingredient-dot"></div><span class="ingredient-name">Macha</span></div>
    <div class="ingredient" style="left:893px; top:743px;"><div class="ingredient-dot"></div><span class="ingredient-name">Ginger</span></div>
    <div class="ingredient" style="left:1091px; top:625px;"><div class="ingredient-dot"></div><span class="ingredient-name">Turmeric</span></div>

    <div class="benefit-band"><span class="benefit">WEIGHT LOSS  ALTERNATIVE !</span></div>
    <div class="count">120 Capsules</div>
  </div>
</body>
</html>
```